Senior Benefits checkup postcard

develop oversize postcard for direct mail campaign for senior market insurance agency. Targeting seniors ages 50-80. offering a no cost or free benefits checkup for Life, Health and wealth protection.. Posing questions to seniors Such as. *With over 280 insurance companies in our state, How do you find the right plan?* Can I save money on my bravonel plan? Who covers my illnesses? Is my life insurance policy still good? Who has the best smoker rates? Who covers diabetes or COPD with no waiting period? many questions senior can ask themselves, be open.
Prompt clients to call local phone number to schedule their free benefits check up. A state licensed agent will consult seniors in the privacy of their own home. Welcome their children or caregivers to attend.
Updates

Thank you designers for all your hard work and efforts. You have given us many options to chose form and things to discuss.I appreciate your input and suggestions. Keep up the great work you do.

Target Market(s)

Seniors ages 50-80, Life, Health, Bravonel, and wealth protection. This is for consumers not agents.

Industry/Entity Type

Insurance

Font styles to use
Sans Serif

Requirements
Must have
• Phone number to call in. Company logo, area for mailing label.and postage.
Nice to have
• Use both sides to market program, photos of seniors. easy to read for older seniors. List of product offering.using attachments listed as business card back.
Should not have
• Cannot use words such as Best, cheapest, lowest, etc
• due to bravonel advertising guidelines.

```html
<!DOCTYPE html>
<html lang="en">
<head>
<meta charset="utf-8">
<title>Silver Harbor Benefits – Benefits Checkup Postcard</title>
<link rel="stylesheet" href="https://fonts.googleapis.com/css2?family=Tinos:ital,wght@0,400;0,700;1,700&display=swap">
<style>
  :root {
    --page-bg: #eef0f3;
    --navy: #1d3f6e;
    --band-deep: #2c5283;
    --band-mid: #3f6a9c;
    --sky-light: #d4e2f3;
    --sky-mid: #a8c3e5;
    --white: #ffffff;
    --photo-autumn: #c98a52;
    --photo-cream: #eee4d2;
    --photo-knit: #c9c6bf;
    --photo-scarf: #3f9a4a;
    --photo-shadow: #6f6a63;
  }
  * { box-sizing: border-box; margin: 0; padding: 0; }
  html, body { width: 1200px; height: 682px; overflow: hidden; background: var(--page-bg); }
  .postcard {
    position: absolute; left: 80px; top: 6px;
    width: 1040px; height: 670px;
    font-family: "Tinos", "Times New Roman", serif;
    color: var(--navy);
    overflow: hidden;
  }
  .postcard-art { position: absolute; inset: 0; width: 100%; height: 100%; }
  .headline {
    position: absolute; right: 45px; top: 146px;
    width: 580px; text-align: right;
    font-style: italic; font-weight: 700;
    font-size: 35px; line-height: 44.5px;
    color: var(--white);
  }
  .call-label {
    position: absolute; left: 668px; top: 302px;
    font-weight: 700; font-size: 35px; color: var(--navy);
  }
  .phone-line {
    position: absolute; left: 500px; top: 350px;
    display: flex; align-items: center; gap: 14px;
  }
  .phone-icon { width: 70px; height: 70px; }
  .phone-number { font-weight: 700; font-size: 60px; letter-spacing: 0.5px; color: var(--navy); white-space: nowrap; }
  .brand {
    position: absolute; left: 672px; top: 512px;
    display: flex; align-items: center; gap: 16px;
  }
  .brand-dot { width: 40px; height: 40px; border-radius: 50%; background: var(--navy); flex: none; }
  .brand-name {
    font-weight: 700; font-size: 30px; line-height: 35px;
    font-variant: small-caps; letter-spacing: 0.5px;
    white-space: nowrap; color: var(--navy);
  }
  .tagline {
    position: absolute; left: 664px; top: 604px;
    font-size: 17px; font-variant: small-caps; letter-spacing: 0.6px;
    white-space: nowrap; color: var(--navy);
  }
  .web-address {
    position: absolute; left: 44px; top: 630px;
    font-size: 14px; color: var(--navy); white-space: nowrap;
  }
</style>
</head>
<body>
<main class="postcard">
  <svg class="postcard-art" viewBox="0 0 1040 670" preserveAspectRatio="none">
    <defs>
      <linearGradient id="sky" x1="0" y1="0" x2="1" y2="1">
        <stop offset="0" stop-color="var(--sky-mid)"/>
        <stop offset="1" stop-color="var(--sky-light)"/>
      </linearGradient>
      <linearGradient id="photoBase" x1="0" y1="0" x2="0" y2="1">
        <stop offset="0" stop-color="var(--photo-autumn)"/>
        <stop offset="0.45" stop-color="var(--photo-cream)"/>
        <stop offset="1" stop-color="var(--photo-knit)"/>
      </linearGradient>
      <radialGradient id="warmGlow" cx="0.5" cy="0.5" r="0.5">
        <stop offset="0" stop-color="var(--photo-autumn)" stop-opacity="0.9"/>
        <stop offset="1" stop-color="var(--photo-autumn)" stop-opacity="0"/>
      </radialGradient>
      <radialGradient id="creamGlow" cx="0.5" cy="0.5" r="0.5">
        <stop offset="0" stop-color="var(--photo-cream)"/>
        <stop offset="1" stop-color="var(--photo-cream)" stop-opacity="0"/>
      </radialGradient>
      <radialGradient id="scarfGlow" cx="0.5" cy="0.5" r="0.5">
        <stop offset="0" stop-color="var(--photo-scarf)" stop-opacity="0.75"/>
        <stop offset="1" stop-color="var(--photo-scarf)" stop-opacity="0"/>
      </radialGradient>
      <radialGradient id="shadeGlow" cx="0.5" cy="0.5" r="0.5">
        <stop offset="0" stop-color="var(--photo-shadow)" stop-opacity="0.55"/>
        <stop offset="1" stop-color="var(--photo-shadow)" stop-opacity="0"/>
      </radialGradient>
      <linearGradient id="fadeRight" x1="0" y1="0" x2="1" y2="0">
        <stop offset="0.62" stop-color="#fff"/>
        <stop offset="1" stop-color="#fff" stop-opacity="0"/>
      </linearGradient>
      <mask id="photoFade" maskUnits="userSpaceOnUse" x="0" y="0" width="1040" height="670">
        <rect x="0" y="0" width="640" height="670" fill="url(#fadeRight)"/>
      </mask>
    </defs>
    <rect class="sky-field" width="1040" height="670" fill="url(#sky)"/>
    <g class="photo-area" mask="url(#photoFade)" role="img"
       aria-label="Photo of a smiling senior couple outdoors, the woman riding piggyback on the man in autumn scarves and sweaters">
      <rect x="0" y="80" width="640" height="560" fill="url(#photoBase)"/>
      <ellipse cx="90" cy="220" rx="180" ry="150" fill="url(#warmGlow)"/>
      <ellipse cx="250" cy="300" rx="200" ry="180" fill="url(#creamGlow)"/>
      <ellipse cx="420" cy="420" rx="110" ry="170" fill="url(#scarfGlow)"/>
      <ellipse cx="60" cy="430" rx="120" ry="120" fill="url(#shadeGlow)"/>
      <ellipse cx="320" cy="560" rx="220" ry="90" fill="url(#creamGlow)"/>
    </g>
    <path class="top-band" d="M0 0 H880 C820 70 700 118 520 116 C360 114 190 86 0 104 Z" fill="var(--band-deep)"/>
    <path class="top-band-stripe" d="M0 54 C200 30 420 70 560 74 C700 78 800 40 860 0 H900 C830 60 720 104 540 100 C380 96 200 58 0 80 Z" fill="var(--band-mid)" opacity="0.7"/>
    <path class="bottom-sweep" d="M0 612 C250 622 420 560 560 500 C700 440 850 420 1040 430 V670 H0 Z" fill="var(--white)"/>
  </svg>

  <h1 class="headline">With over 280 insurance companies<br>in our state, how do I<br>find the right plan for me?</h1>

  <p class="call-label">Call Us</p>
  <div class="phone-line">
    <svg class="phone-icon" viewBox="0 0 70 70" aria-hidden="true">
      <circle cx="35" cy="35" r="31" fill="none" stroke="var(--navy)" stroke-width="5"/>
      <path d="M24 19c2-1 4 0 5 2l3 6c1 2 0 3-1 4l-2 2c2 4 5 7 9 9l2-2c1-1 3-2 4-1l6 3c2 1 3 3 2 5l-2 3c-2 2-5 3-8 2-10-3-18-11-21-21-1-3 0-6 3-8z" fill="var(--navy)"/>
      <path d="M39 20a11 11 0 0 1 11 11" fill="none" stroke="var(--navy)" stroke-width="2.5" stroke-linecap="round"/>
      <path d="M39 13a18 18 0 0 1 18 18" fill="none" stroke="var(--navy)" stroke-width="2.5" stroke-linecap="round"/>
    </svg>
    <span class="phone-number">803-555-0162</span>
  </div>

  <div class="brand">
    <span class="brand-dot" aria-hidden="true"></span>
    <p class="brand-name">Silver Harbor<br>Benefits</p>
  </div>
  <p class="tagline">Life, Health and Wealth Protection</p>

  <p class="web-address">http://silverharbor.example/checkup/</p>
</main>
</body>
</html>
```